Gutschein-Design Falter Webshop
Zielgruppe
Webshop von Pyrotechnischen Artikeln. Rauchkörper, Bengalische Lichter, Kinderfeuerwerk, klassisches Silvesterfeuerwerk. Der Shop ist zu finden unter https://www.funkenkiste-beispiel.de
Das Format sollte sich an DIN Lang orientieren.
Wenn Artikelbilder oder sonstige Fotos aus dem Shop benötigt werden, können diese gerne angefragt werden.
Aufgabenstellung
Der Shop sollte im Flyer wieder erkennbar sein und nach Möglichkeit alle 5 Hauptkategorien abbilden.
Wobei Silvesterfeuerwerk, Zubehör und Partyartikel die kleinere Rolle spielen.
Rauch und Bengal stehen dabei im Vordergrund
Ein Textfeld sollte enthalten sein, worein wir dann den Gutscheincode / Wert drucken.
Edit: Sorry, ich hatte anfangs die falschen Grafiken hochgeladen. Jetzt ist das Shoplogo in den Files zu finden. Ebenso ein Beispielfoto mit Rauch

```html
<!DOCTYPE html>
<html lang="de">
<head>
<meta charset="utf-8">
<title>Gutschein – Falter Webshop</title>
<link rel="stylesheet" href="https://fonts.googleapis.com/css2?family=Exo+2:wght@400&display=swap">
<style>
  :root {
    --page-bg: #ececec;
    --night: #0b0d1c;
    --night-violet: #2a2140;
    --spark-violet: #8f7fd8;
    --spark-white: #eae6ff;
    --stone-gold: #c99a4e;
    --stone-dark: #6a4a22;
    --brand-copper: #c8874a;
    --text-light: #ffffff;
    --field-white: #ffffff;
  }
  * { box-sizing: border-box; margin: 0; padding: 0; }
  html, body {
    width: 1200px; height: 1200px; overflow: hidden;
    background: var(--page-bg);
    font-family: "Exo 2", sans-serif;
  }
  .voucher {
    position: absolute;
    left: 129px;
    width: 956px;
    height: 477px;
    overflow: hidden;
    background: var(--night);
  }
  .voucher--front { top: 98px; }
  .voucher--back { top: 627px; }

  .voucher__photo {
    position: absolute; inset: 0;
    background:
      radial-gradient(ellipse 30% 40% at 82% 30%, rgba(234,230,255,0.75), transparent 70%),
      radial-gradient(ellipse 45% 60% at 75% 45%, rgba(143,127,216,0.55), transparent 75%),
      radial-gradient(ellipse 55% 45% at 30% 100%, var(--stone-gold), rgba(106,74,34,0.6) 55%, transparent 80%),
      linear-gradient(100deg, var(--night) 0%, var(--night) 35%, var(--night-violet) 100%);
  }

  .brand {
    position: absolute;
    display: flex; align-items: center; gap: 10px;
    color: var(--brand-copper);
    font-weight: 400;
    line-height: 1.2;
    letter-spacing: 1px;
    white-space: nowrap;
  }
  .brand__dot {
    width: 16px; height: 16px; border-radius: 50%;
    background: var(--brand-copper);
  }
  .voucher--front .brand { left: 490px; top: 100px; transform: translateX(-50%); font-size: 44px; }
  .voucher--back .brand { left: 38px; top: 180px; font-size: 44px; }

  .voucher__band {
    position: absolute; left: 300px; right: 0; top: 166px; height: 161px;
    background: linear-gradient(90deg, rgba(255,255,255,0) 0%, rgba(255,255,255,0.18) 40%, rgba(255,255,255,0.12) 100%);
  }
  .voucher__title {
    position: absolute; left: 0; right: 0; top: 170px;
    text-align: center;
    padding-left: 30px;
    color: var(--text-light);
    font-size: 142px;
    line-height: 1;
    letter-spacing: -6px;
    font-weight: 400;
    white-space: nowrap;
  }

  .categories {
    position: absolute; left: 0; right: 0; top: 28px;
    text-align: center;
    color: var(--text-light);
    font-size: 29px;
    letter-spacing: 0.5px;
    white-space: nowrap;
  }
  .field {
    position: absolute;
    background: var(--field-white);
    border-radius: 16px;
  }
  .field--value { left: 356px; top: 93px; width: 577px; height: 244px; }
  .field--code { left: 440px; top: 368px; width: 493px; height: 85px; border-radius: 12px; }
</style>
</head>
<body>
  <section class="voucher voucher--front">
    <div class="voucher__photo" role="img" aria-label="Nachtfoto: beleuchtetes Stadttor mit violettem Feuerwerk am Himmel"></div>
    <div class="brand"><span class="brand__dot"></span>Falterwerk</div>
    <div class="voucher__band"></div>
    <h1 class="voucher__title">GUTSCHEIN</h1>
  </section>

  <section class="voucher voucher--back">
    <div class="voucher__photo" role="img" aria-label="Nachtfoto: beleuchtetes Stadttor mit violettem Feuerwerk am Himmel"></div>
    <p class="categories">BENGAL | RAUCHKÖRPER | PARTYARTIKEL | FEUERWERK | ZUBEHÖR</p>
    <div class="brand"><span class="brand__dot"></span>Falterwerk</div>
    <div class="field field--value"></div>
    <div class="field field--code"></div>
  </section>
</body>
</html>
```